Poised Coach website development

Need a website designed for a coaching business. Very high-end, luxury, professionalism, in the area of STRESS, see brief attached. I have a logo already
Updates

Slow in providing feedback

Target Market(s)

CEOs very successful men and wealthy females, high end luxury market

Industry/Entity Type

coaching

Number of Pages Required

1 page

Requirements
Must have
• Luxury look, professional, serious but warm, appealing to both sexes

```html
<!DOCTYPE html>
<html lang="en">
<head>
<meta charset="utf-8">
<title>Poised Coach — Executive Coaching</title>
<link rel="stylesheet" href="https://fonts.googleapis.com/css2?family=Poppins:wght@500;600;700&family=Roboto:wght@400;500&display=swap">
<style>
:root{
  --ink:#141414;
  --text:#3a3a3a;
  --white:#ffffff;
  --blue:#0b6cc3;
  --blue-dark:#0a5fae;
  --icon:#1f6fc4;
  --accent:#f5b53a;
  --cream:#fdf1dd;
  --sky:#dde8f4;
  --footer:#231f20;
}
*{margin:0;padding:0;box-sizing:border-box}
html,body{width:1200px;height:4792px;overflow:hidden}
body{position:relative;background:var(--white);font-family:'Roboto',Arial,sans-serif;color:var(--text)}
h1,h2,h3,.brand,.athlete-label{font-family:'Poppins',Arial,sans-serif;color:var(--ink)}
.abs{position:absolute}
.hex{clip-path:polygon(50% 0,100% 25%,100% 75%,50% 100%,0 75%,0 25%)}
p,li{font-size:14px;line-height:21px}

/* header */
.brand{position:absolute;left:66px;top:20px;width:240px;text-align:center;white-space:nowrap}
.brand-mark{width:34px;height:34px;background:var(--ink);margin:0 auto 10px}
.brand-name{font-size:16px;font-weight:600;letter-spacing:5px;color:var(--ink)}
.menu-toggle{position:absolute;left:1083px;top:26px;width:26px}
.menu-toggle span{display:block;height:2px;background:var(--ink);margin-bottom:6px;margin-left:auto}

/* hero */
.hero-photo{left:592px;top:0;width:608px;height:753px;background:linear-gradient(160deg,#eceef0 0%,#d9dde0 40%,#c9d3cf 70%,#e8e6e3 100%);clip-path:polygon(0 0,100% 0,100% 72%,60% 100%,0 80%)}
.hero-kicker{left:87px;top:314px;font-family:'Poppins',sans-serif;font-weight:600;font-size:19px;color:var(--ink)}
.hero-title{left:86px;top:340px;font-size:58px;line-height:64px;font-weight:700;white-space:nowrap;z-index:2}

/* head coach */
.coach-photo{left:71px;top:748px;width:470px;height:540px;background:linear-gradient(170deg,#dfe9ec 0%,#a9b8a7 45%,#6e5a49 100%)}
.coach-title{left:596px;top:848px;font-size:46px;font-weight:700}
.coach-copy{left:599px;top:913px;width:505px}
.coach-copy p{margin-bottom:8px}

/* audience panels */
.panel{top:1371px;height:549px;width:600px}
.panel-women{left:0;background:var(--cream)}
.panel-men{left:595px;width:605px;background:var(--sky)}
.panel .art{position:absolute;border-radius:8px}
.panel-women .art{left:117px;top:80px;width:342px;height:217px;background:radial-gradient(circle at 50% 55%,#f4c9a6 0%,#f8dcc0 55%,var(--cream) 100%)}
.panel-men .art{left:112px;top:86px;width:390px;height:212px;background:radial-gradient(circle at 50% 55%,#bcd1ec 0%,#cfdef1 55%,var(--sky) 100%)}
.panel h2{position:absolute;top:325px;font-size:37px;font-weight:700}
.panel p{position:absolute;top:378px;width:435px}
.panel-women h2,.panel-women p{left:84px}
.panel-men h2,.panel-men p{left:95px}

/* athletes */
.athletes-title{left:0;width:1200px;top:2034px;text-align:center;font-size:42px;font-weight:700}
.athlete{position:absolute;top:2118px;width:150px;text-align:center}
.athlete-hex{width:140px;height:150px;margin:0 auto;filter:drop-shadow(0 4px 10px rgba(0,0,0,.10))}
.athlete-hex .inner{width:140px;height:150px;background:var(--white);display:flex;align-items:center;justify-content:center}
.athlete-hex svg{width:72px;height:72px;fill:none;stroke:var(--icon);stroke-width:3;stroke-linecap:round;stroke-linejoin:round}
.athlete-hex svg .hl{stroke:var(--accent)}
.athlete-hex svg .hl-fill{fill:var(--accent);stroke:none}
.athlete-label{margin-top:10px;font-size:13px;font-weight:600;white-space:nowrap}

/* challenges */
.challenge-photo{left:593px;top:2400px;width:510px;height:561px;background:linear-gradient(180deg,#6f9a6a 0%,#8fb18a 35%,#6b4a3a 60%,#b9844e 100%)}
.challenge-card{left:82px;top:2470px;width:511px;height:521px;background:var(--white);box-shadow:0 8px 30px rgba(0,0,0,.08);z-index:2}
.challenge-card h2{position:absolute;left:73px;top:150px;font-size:44px;font-weight:700}
.challenge-card .copy{position:absolute;left:73px;top:222px;width:360px}
.challenge-card p{margin-bottom:10px}

/* blue band */
.band{left:0;top:2961px;width:1200px;height:685px;background:linear-gradient(180deg,var(--blue) 0%,var(--blue-dark) 100%)}
.band h2{position:absolute;color:var(--white);font-size:42px;font-weight:700}
.band ul{position:absolute;list-style:none;color:#e6effa}
.band li{position:relative;padding-left:24px;margin-bottom:10px;font-size:13.5px}
.band li::before{content:"";position:absolute;left:2px;top:7px;width:7px;height:7px;border-radius:50%;background:#7fb3e6}
.why-title{left:87px;top:226px}
.why-list{left:87px;top:300px;width:460px}
.benefits-title{left:629px;top:178px}
.benefits-list{left:629px;top:251px;width:470px}

/* welcome */
.welcome-photo{left:82px;top:3757px;width:468px;height:536px;background:linear-gradient(160deg,#8a7561 0%,#5a4536 45%,#2d2420 100%)}
.welcome-title{left:596px;top:3882px;font-size:44px;line-height:48px;font-weight:700}
.welcome-copy{left:597px;top:3996px;width:505px}

/* footer */
.footer{left:0;top:4392px;width:1200px;height:400px;background:var(--footer);color:var(--white)}
.footer .brand{left:400px;top:80px;width:400px}
.footer .brand-mark{background:var(--white)}
.footer .brand-name{color:var(--white);font-size:20px;letter-spacing:6px}
.footer-nav{position:absolute;left:0;width:1200px;top:194px;text-align:center;font-size:14px}
.footer-nav a{color:var(--white);text-decoration:none;margin:0 9px}
.socials{position:absolute;left:0;width:1200px;top:230px;display:flex;justify-content:center;gap:8px}
.socials span{width:32px;height:32px;border-radius:50%}
.footer-rule{position:absolute;left:87px;top:314px;width:1026px;height:1px;background:#3d3839}
.copyright{position:absolute;left:0;width:1200px;top:356px;text-align:center;font-size:14px}
.to-top{position:absolute;left:1126px;top:316px;width:38px;height:38px;border-radius:50%;background:var(--blue)}
</style>
</head>
<body>

<header>
  <div class="brand"><div class="brand-mark"></div><div class="brand-name">POISED COACH</div></div>
  <div class="menu-toggle" aria-label="Menu"><span style="width:26px"></span><span style="width:18px"></span><span style="width:26px"></span></div>
</header>

<section class="hero">
  <div class="abs hero-photo" role="img" aria-label="Smiling woman in a striped sweater working on a laptop at a bright desk"></div>
  <div class="abs hero-kicker">Career, Health, Leadership</div>
  <h1 class="abs hero-title">Executive<br>Coaching Can<br>Reduce Your Stress</h1>
</section>

<section class="coach">
  <div class="abs hex coach-photo" role="img" aria-label="Coach presenting to a seated audience"></div>
  <h2 class="abs coach-title">Head Coach</h2>
  <div class="abs coach-copy">
    <p>Not your typical “quiet whale music playing in the background, kind of “stress guy”....stress is good, it can save your life...teach people to look at stress in a new light, to understand it, recognize when it is coming on, and decide to use it for performance, or control it...</p>
    <p>My desire is to help those in stress, recognize the signs of stress and how to channel the stress correctly.</p>
    <p>Provide techniques to reduce “bad” stress</p>
    <p>My focus will be releasing stress and channeling it through wellness activities. Mindfulness, and knowing yourself, self-awareness</p>
    <p>Not necessarily stress reduction but stress enhancement</p>
    <p>I only have one job and that is to help clients think differently. Everything else is just fluff</p>
  </div>
</section>

<section>
  <div class="abs panel panel-women">
    <div class="art" role="img" aria-label="Illustration of a woman surrounded by thought bubbles of worry"></div>
    <h2>Women</h2>
    <p>General issues...I live near very wealthy neighborhoods with lots of “trophy wives” who are really quite lonely, as husbands work a great deal. They are also concerned with “fitting in” and acceptance...using wellness, yoga, aromatherapy,</p>
  </div>
  <div class="abs panel panel-men">
    <div class="art" role="img" aria-label="Illustration of a stressed man sitting beside stacks of paperwork"></div>
    <h2>Men</h2>
    <p>The stress of success...they cannot share with anyone in fear of showing weakness...or a chink in the armor...not fully fulfilled, will provide and/or sign a confidentiality agreement.<br>Fish where the big fish are: hedge fund companies: Ashbury is the epi center.</p>
  </div>
</section>

<section>
  <h2 class="abs athletes-title">Athletes</h2>

  <div class="athlete" style="left:135px"><div class="athlete-hex hex"><div class="inner hex">
    <svg viewBox="0 0 64 64" aria-hidden="true"><circle cx="32" cy="32" r="24"/><path class="hl" d="M35 14 24 34h9l-4 16 12-22h-9z"/></svg>
  </div></div><div class="athlete-label">Performance stress</div></div>

  <div class="athlete" style="left:291px"><div class="athlete-hex hex"><div class="inner hex">
    <svg viewBox="0 0 64 64" aria-hidden="true"><path d="M12 18h40M12 32h40M12 46h40"/><circle class="hl" cx="22" cy="18" r="5"/><circle class="hl" cx="42" cy="32" r="5"/><circle class="hl" cx="28" cy="46" r="5"/></svg>
  </div></div><div class="athlete-label">Control</div></div>

  <div class="athlete" style="left:448px"><div class="athlete-hex hex"><div class="inner hex">
    <svg viewBox="0 0 64 64" aria-hidden="true"><path d="M8 18V8h10M46 8h10v10M56 46v10H46M18 56H8V46"/><circle cx="32" cy="32" r="14"/><path d="M32 12v10M32 42v10M12 32h10M42 32h10"/><circle class="hl-fill" cx="32" cy="32" r="4"/></svg>
  </div></div><div class="athlete-label">Focus</div></div>

  <div class="athlete" style="left:602px"><div class="athlete-hex hex"><div class="inner hex">
    <svg viewBox="0 0 64 64" aria-hidden="true"><path d="M6 32s10-16 26-16 26 16 26 16-10 16-26 16S6 32 6 32z"/><circle class="hl" cx="32" cy="32" r="8"/><circle class="hl-fill" cx="32" cy="32" r="3"/></svg>
  </div></div><div class="athlete-label">Visualization</div></div>

  <div class="athlete" style="left:758px"><div class="athlete-hex hex"><div class="inner hex">
    <svg viewBox="0 0 64 64" aria-hidden="true"><circle class="hl" cx="32" cy="12" r="5"/><path d="M32 17v39M22 26h20M12 38c0 10 9 18 20 18s20-8 20-18M8 42l4-5 5 4M56 42l-4-5-5 4"/></svg>
  </div></div><div class="athlete-label">Anchoring</div></div>

  <div class="athlete" style="left:915px"><div class="athlete-hex hex"><div class="inner hex">
    <svg viewBox="0 0 64 64" aria-hidden="true"><path d="M8 24h30a7 7 0 1 0-7-7"/><path class="hl" d="M8 34h42a6 6 0 1 1-6 6"/><path d="M8 44h22a6 6 0 1 1-6 6"/></svg>
  </div></div><div class="athlete-label">Breathing</div></div>
</section>

<section>
  <div class="abs challenge-photo" role="img" aria-label="Group of smiling colleagues around a wooden table with a laptop and coffee"></div>
  <div class="abs challenge-card">
    <h2>Challenges</h2>
    <div class="copy">
      <p>Designing website that resonates with both men and women...or do I bifurcate the home screen “Men click here” Women click here”? The photos of me for the female market will be causal in the house, holding a cup of coffee, etc. laughing, lots of expression, someone easy to share and be open with.</p>
      <p>Men side: a bit more formal, authoritative, trusting,</p>
    </div>
  </div>
</section>

<section class="abs band">
  <h2 class="why-title">Why me?</h2>
  <ul class="why-list">
    <li>Been there done that! Have been through a lot, started businesses, selling a business, law suits, marriage, divorce, second marriage, kids, school, sports, fights, robbed, gun in face, traveled the world, successful, two great kids (both Cadets at Northfield Academy...duty/honor/country)</li>
    <li>Limited number of clients...different stage of life, empty nester, have a full career...won’t be a number</li>
  </ul>
  <h2 class="benefits-title">Benefits</h2>
  <ul class="benefits-list">
    <li>Experience</li>
    <li>Sector expert Health/Wellness. Presented at numerous industry shows and quoted in national publications (not as a coach, I’m new, but in the health &amp; wellness space)</li>
    <li>Excellent listener...being in sales for many years, the secret is to really listen...and get to the end game, and make it feel as if it was their decision. Not sure how to word this as a benefit.</li>
    <li>Access/resources industry professionals, sport psychologist...just spent a few hours with the Mind performance coach for the Harbor City Gulls baseball team...I can get the best advice and latest techniques in mind/body training performance.</li>
    <li>Private, more than happy to sign confidentiality agreement. Especially for the business man.</li>
  </ul>
</section>

<section>
  <div class="abs hex welcome-photo" role="img" aria-label="Two people in conversation, one gesturing while the other listens"></div>
  <h2 class="abs welcome-title">Welcome to<br>PoisedCoach</h2>
  <p class="abs welcome-copy">Poised Coach came about due to my desire to help people lead a better and healthier life. Initially, I was involved in the fitness/body side of health. As years passed and my experience grew, I realized how important the mind was in total wellness, and that the mind is all powerful and controlling. Control the mind, control the body and achieve success. Stress can be the most debilating factor in our lives, it is the root cause of so many diseases and costs the US workplace an estimated 300 billion dollars due to loss of productivity.</p>
</section>

<footer class="abs footer">
  <div class="brand"><div class="brand-mark"></div><div class="brand-name">POISED COACH</div></div>
  <nav class="footer-nav"><a href="#">Home</a><a href="#">About</a><a href="#">Benefits</a><a href="#">Athletes</a><a href="#">Contact Us</a></nav>
  <div class="socials">
    <span style="background:#3b5ba5" aria-label="Social link"></span>
    <span style="background:#1da1f2" aria-label="Social link"></span>
    <span style="background:#dc4a38" aria-label="Social link"></span>
    <span style="background:#1c7ab8" aria-label="Social link"></span>
  </div>
  <div class="footer-rule"></div>
  <div class="to-top" aria-label="Back to top">
    <svg width="38" height="38" viewBox="0 0 38 38"><path d="M15 21l4-4 4 4" fill="none" stroke="#fff" stroke-width="2"/></svg>
  </div>
  <div class="copyright">©Copyright 2022 | All Rights Reserved</div>
</footer>

</body>
</html>
```